Speisekarten
Zielgruppe
Die Sola Brisa Kassel ist vorrangig in der hochwertigen Gastronomie und Hotellerie tätig. Unser Leitspruch: IMMER EINEN TICK MEHR ALS ERWARTET. MEHR QUALITÄT, MEHR VIELFALT, MEHR LEISTUNG, MEHR LEIDENSCHAFT IN JEDEM DETAIL.
Was dazu gehört: Eine vielseitige Genießerwelt, die ihresgleichen sucht: Zehn Event-Locations, drei Hotels, zwanzig Tagungsräume, sieben Restaurants, eine Eisbar, zwei Feinkostgeschäfte und einen eigenen Strandabschnitt an der Lahn dürfen wir zu uns zählen.
Ob tagen, erholen, feiern oder genießen, bei uns gibt es das Rundum-Paket.
Aufgabenstellung
Sehr hochwertiges Design einer Speisekarte für ein asiatisches Restaurant der Extraklasse.

```html
<!DOCTYPE html>
<html lang="de">
<head>
<meta charset="utf-8">
<title>OKUVA – Speisekarte</title>
<link href="https://fonts.googleapis.com/css2?family=Nunito+Sans:wght@300;400;800&display=swap" rel="stylesheet">
<style>
  :root {
    --backdrop: #e8e8e8;
    --page: #262626;
    --red: #e0262a;
    --white: #ffffff;
    --muted: #d9d9d9;
    --ink-shadow: #141414;
    --illustration-warm: #4a2c29;
    --illustration-cool: #3a3532;
  }
  * { margin: 0; padding: 0; box-sizing: border-box; }
  html, body { width: 735px; height: 1200px; overflow: hidden; background: var(--backdrop); }
  body { position: relative; font-family: "Nunito Sans", sans-serif; color: var(--white); }

  .page { position: absolute; width: 287px; height: 408px; background: var(--page); overflow: hidden; }
  .cover-sketch { left: 80px; top: 84px; }
  .inside-sketch { left: 393px; top: 192px; }
  .cover-ink { left: 67px; top: 694px; }
  .inside-ink { left: 380px; top: 773px; }

  .art { position: absolute; inset: 0; width: 287px; height: 408px; }

  .cover-label {
    position: absolute; top: 25px; left: 0; width: 100%; text-align: center;
    font-weight: 400; font-size: 8px; letter-spacing: 3px; padding-left: 3px;
  }
  .brand {
    position: absolute; top: 155px; left: 0; width: 100%;
    display: flex; align-items: center; justify-content: center; gap: 6px;
  }
  .brand-name { color: var(--red); font-weight: 800; font-size: 26px; letter-spacing: 3px; line-height: 1; }
  .brand-mark { width: 9px; height: 9px; background: var(--red); }

  .section-heading {
    position: absolute; font-weight: 300; font-size: 8px; letter-spacing: 3.2px; line-height: 10px;
  }
  .section-heading.centered { left: 0; width: 100%; text-align: center; padding-left: 3px; }
  .section-heading.accent { color: var(--red); }

  .item { position: absolute; height: 20px; }
  .item .title { display: block; font-weight: 800; font-size: 7.6px; line-height: 10px; letter-spacing: 0.1px; white-space: nowrap; }
  .item .price { position: absolute; right: 0; top: 0; font-weight: 800; font-size: 7.6px; line-height: 10px; }
  .item .desc { display: block; font-weight: 400; font-size: 5.7px; line-height: 9px; color: var(--muted); white-space: nowrap; }

  .recommend-frame { position: absolute; left: 15px; top: 157px; width: 262px; height: 95px; border: 1px solid var(--red); }

  .category-tab {
    position: absolute; left: 229px; top: 25px; width: 33px; height: 136px; border: 1px solid var(--red);
    display: flex; flex-direction: column; align-items: center; justify-content: center; gap: 4.6px;
    color: var(--red); font-weight: 400; font-size: 7px; line-height: 9px;
  }
</style>
</head>
<body>

  <section class="page cover-sketch">
    <svg class="art" viewBox="0 0 287 408" role="img" aria-label="Hand-drawn line illustrations of leek, fish, crab, shrimp, onions, garlic and herbs">
      <defs>
        <linearGradient id="sketchTone" x1="0" y1="0" x2="0" y2="1">
          <stop offset="0" stop-color="var(--illustration-cool)"/>
          <stop offset="1" stop-color="var(--illustration-warm)"/>
        </linearGradient>
      </defs>
      <path d="M262 0 H287 V408 H0 V340 C40 330 90 320 140 300 C170 285 200 260 215 230 C225 200 215 160 235 140 C250 120 250 80 262 0 Z" fill="url(#sketchTone)" opacity="0.75"/>
    </svg>
    <p class="cover-label">MENU</p>
    <div class="brand"><span class="brand-name">OKUVA</span><span class="brand-mark"></span></div>
  </section>

  <section class="page inside-sketch">
    <svg class="art" viewBox="0 0 287 408" role="img" aria-label="Red line illustration of a shrimp">
      <path d="M176 30 C200 18 250 14 287 18 V90 C250 100 210 100 186 88 C176 70 172 48 176 30 Z" fill="var(--illustration-warm)" opacity="0.55"/>
    </svg>
    <p class="section-heading centered" style="top:25px">STARTERS</p>

    <div class="item" style="left:24px;top:60px;width:113px"><span class="title">DAS IST EIN TITEL</span><span class="price">9</span><span class="desc">Lorem ipsum dolor sit amet</span></div>
    <div class="item" style="left:151px;top:60px;width:113px"><span class="title">DAS IST EIN TITEL</span><span class="price">9</span><span class="desc">Lorem ipsum dolor sit amet</span></div>
    <div class="item" style="left:24px;top:89px;width:113px"><span class="title">DAS IST EIN TITEL</span><span class="price">9</span><span class="desc">Lorem ipsum dolor sit amet</span></div>
    <div class="item" style="left:151px;top:89px;width:113px"><span class="title">DAS IST EIN TITEL</span><span class="price">9</span><span class="desc">Lorem ipsum dolor sit amet</span></div>
    <div class="item" style="left:24px;top:118px;width:113px"><span class="title">DAS IST EIN TITEL</span><span class="price">9</span><span class="desc">Lorem ipsum dolor sit amet</span></div>
    <div class="item" style="left:151px;top:118px;width:113px"><span class="title">DAS IST EIN TITEL</span><span class="price">9</span><span class="desc">Lorem ipsum dolor sit amet</span></div>

    <div class="recommend-frame"></div>
    <p class="section-heading centered accent" style="top:168px">– EMPFEHLUNGEN –</p>
    <div class="item" style="left:24px;top:188px;width:113px"><span class="title">DAS IST EIN TITEL</span><span class="price">9</span><span class="desc">Lorem ipsum dolor sit amet</span></div>
    <div class="item" style="left:151px;top:188px;width:113px"><span class="title">DAS IST EIN TITEL</span><span class="price">9</span><span class="desc">Lorem ipsum dolor sit amet</span></div>
    <div class="item" style="left:24px;top:217px;width:113px"><span class="title">DAS IST EIN TITEL</span><span class="price">9</span><span class="desc">Lorem ipsum dolor sit amet</span></div>
    <div class="item" style="left:151px;top:217px;width:113px"><span class="title">DAS IST EIN TITEL</span><span class="price">9</span><span class="desc">Lorem ipsum dolor sit amet</span></div>

    <p class="section-heading centered" style="top:278px">VEGATARIAN</p>
    <div class="item" style="left:24px;top:305px;width:113px"><span class="title">DAS IST EIN TITEL</span><span class="price">9</span><span class="desc">Lorem ipsum dolor sit amet</span></div>
    <div class="item" style="left:151px;top:305px;width:113px"><span class="title">DAS IST EIN TITEL</span><span class="price">9</span><span class="desc">Lorem ipsum dolor sit amet</span></div>
    <div class="item" style="left:24px;top:334px;width:113px"><span class="title">DAS IST EIN TITEL</span><span class="price">9</span><span class="desc">Lorem ipsum dolor sit amet</span></div>
    <div class="item" style="left:151px;top:334px;width:113px"><span class="title">DAS IST EIN TITEL</span><span class="price">9</span><span class="desc">Lorem ipsum dolor sit amet</span></div>
    <div class="item" style="left:24px;top:363px;width:113px"><span class="title">DAS IST EIN TITEL</span><span class="price">9</span><span class="desc">Lorem ipsum dolor sit amet</span></div>
  </section>

  <section class="page cover-ink">
    <svg class="art" viewBox="0 0 287 408" role="img" aria-label="Large black brush-painted Japanese character for water">
      <defs>
        <linearGradient id="inkTone" x1="0" y1="0" x2="0" y2="1">
          <stop offset="0" stop-color="var(--ink-shadow)" stop-opacity="0.6"/>
          <stop offset="1" stop-color="var(--ink-shadow)"/>
        </linearGradient>
      </defs>
      <rect x="62" y="215" width="225" height="193" fill="url(#inkTone)" opacity="0.8"/>
    </svg>
    <p class="cover-label">MENU</p>
    <div class="brand"><span class="brand-name">OKUVA</span><span class="brand-mark"></span></div>
  </section>

  <section class="page inside-ink">
    <svg class="art" viewBox="0 0 287 408" role="img" aria-label="Black brush-painted Japanese character for water">
      <defs>
        <linearGradient id="inkToneInside" x1="0" y1="0" x2="0" y2="1">
          <stop offset="0" stop-color="var(--ink-shadow)" stop-opacity="0.5"/>
          <stop offset="1" stop-color="var(--ink-shadow)"/>
        </linearGradient>
      </defs>
      <rect x="63" y="274" width="224" height="134" fill="url(#inkToneInside)" opacity="0.8"/>
    </svg>

    <p class="section-heading accent" style="left:24px;top:25px">SEAFOOD</p>
    <div class="item" style="left:24px;top:51px;width:182px"><span class="title">DAS IST EIN TITEL</span><span class="price">9</span><span class="desc">Lorem ipsum dolor sit amet</span></div>
    <div class="item" style="left:24px;top:80px;width:182px"><span class="title">DAS IST EIN TITEL</span><span class="price">9</span><span class="desc">Lorem ipsum dolor sit amet, consetetur sadipscing</span></div>
    <div class="item" style="left:24px;top:109px;width:182px"><span class="title">DAS IST EIN TITEL</span><span class="price">9</span><span class="desc">Lorem ipsum dolor sit amet, consetetur elitr</span></div>
    <div class="item" style="left:24px;top:139px;width:182px"><span class="title">DAS IST EIN TITEL</span><span class="price">9</span><span class="desc">Lorem ipsum dolor sit amet, consetetur sadipscing elitr</span></div>

    <div class="category-tab"><span>S</span><span>T</span><span>A</span><span>R</span><span>T</span><span>E</span><span>R</span><span>S</span></div>

    <p class="section-heading accent" style="left:24px;top:194px">VEGETARIAN</p>
    <div class="item" style="left:24px;top:223px;width:113px"><span class="title">DAS IST EIN TITEL</span><span class="price">9</span><span class="desc">Lorem ipsum dolor sit amet</span></div>
    <div class="item" style="left:151px;top:223px;width:113px"><span class="title">DAS IST EIN TITEL</span><span class="price">9</span><span class="desc">Lorem ipsum dolor sit amet</span></div>
    <div class="item" style="left:24px;top:252px;width:113px"><span class="title">DAS IST EIN TITEL</span><span class="price">9</span><span class="desc">Lorem ipsum dolor sit amet</span></div>
    <div class="item" style="left:151px;top:252px;width:113px"><span class="title">DAS IST EIN TITEL</span><span class="price">9</span><span class="desc">Lorem ipsum dolor sit amet</span></div>

    <p class="section-heading accent" style="left:24px;top:305px">CHICKEN</p>
    <div class="item" style="left:24px;top:329px;width:113px"><span class="title">DAS IST EIN TITEL</span><span class="price">9</span><span class="desc">Lorem ipsum dolor sit amet</span></div>
    <div class="item" style="left:151px;top:329px;width:113px"><span class="title">DAS IST EIN TITEL</span><span class="price">9</span><span class="desc">Lorem ipsum dolor sit amet</span></div>
    <div class="item" style="left:24px;top:357px;width:113px"><span class="title">DAS IST EIN TITEL</span><span class="price">9</span><span class="desc">Lorem ipsum dolor sit amet</span></div>
    <div class="item" style="left:151px;top:357px;width:113px"><span class="title">DAS IST EIN TITEL</span><span class="price">9</span><span class="desc">Lorem ipsum dolor sit amet</span></div>
  </section>

</body>
</html>
```